7 ¾ long by 5 inches high print ad

I have a 1/2 page ad for a print magazine I need to be designed. Uploaded is the previous year design. We want something to be more aligned with our new website look/feel and new messaging from website.

I have provided some photos, the logo, color codes and a recent banner ad sample for copy.

Target Market(s)

Developers

Font styles to use
Sans Serif

Requirements
Must have
• Clear headline, sub headline, and value statement
• Services to highlight, Tilt-Up Construction,
• Website, phone, social icons, Facebook, Twitter, and LinkedIn
Nice to have
• https://marrowcrestbuilding.com/
• Some of the logos in the clients who trust us section

```html
<!DOCTYPE html>
<html lang="en">
<head>
<meta charset="utf-8">
<title>Marrowcrest Construction – Half Page Ad</title>
<link rel="stylesheet" href="https://fonts.googleapis.com/css2?family=Open+Sans:wght@300;400;600;700;800&family=Montserrat:wght@400;500&display=swap">
<style>
  :root {
    --navy: #19203f;
    --orange: #e8961e;
    --orange-deep: #de8a14;
    --paper: #f0f0f0;
    --ink: #3a3b40;
    --white: #ffffff;
    --shade: rgba(20, 22, 30, 0.72);
    --social-a: #2aa3e6;
    --social-b: #3a5a9a;
    --social-c: #1499d4;
  }
  * { box-sizing: border-box; margin: 0; padding: 0; }
  html, body {
    width: 885px; height: 1200px; overflow: hidden;
    background: var(--white);
    font-family: "Open Sans", Arial, sans-serif;
  }
  .ad {
    position: absolute; left: 47px;
    width: 988px; height: 639px;
    transform: scale(0.8045); transform-origin: top left;
    overflow: hidden; background: var(--paper);
  }
  .ad--retail { top: 55px; }
  .ad--tiltup { top: 651px; }

  .promise {
    position: absolute; left: 408px; top: 0; width: 580px; height: 129px;
    padding: 32px 0 0 19px;
    font-size: 23px; font-weight: 700; line-height: 24px; color: var(--ink);
    text-transform: uppercase;
  }
  .promise__accent { color: var(--orange); }

  .headline {
    position: absolute; left: 408px; top: 129px; width: 580px; height: 78px;
    background: var(--orange);
    padding: 10px 0 0 24px;
    font-size: 47px; font-weight: 800; color: var(--white); letter-spacing: 0.3px;
  }

  .photo {
    position: absolute; left: 320px; top: 207px; width: 668px; height: 358px;
  }
  .ad--retail .photo {
    background: linear-gradient(180deg, #8fa6bf 0%, #6f7a5e 14%, #e9ecef 40%, #d8d2c4 62%, #4a4d52 100%);
  }
  .ad--tiltup .photo {
    background: linear-gradient(90deg, #e8e4dc 0%, #3d6f3a 18%, #3f6fd0 30%, #eef0f2 50%, #5a86dc 72%, #8a5a2a 92%, #b57a35 100%);
  }

  .tagline {
    position: absolute; left: 320px; top: 502px; width: 668px; height: 63px;
    background: var(--shade);
    padding: 17px 0 0 41px;
    font-size: 23px; font-weight: 700; color: var(--white); text-transform: uppercase;
  }
  .tagline__accent { color: var(--orange); }

  .panel { position: absolute; left: 0; top: 0; width: 408px; height: 565px; }

  .brand { position: absolute; left: 32px; top: 36px; display: flex; align-items: center; gap: 25px; height: 94px; }
  .brand__mark { width: 58px; height: 58px; background: var(--orange); flex: none; }
  .brand__name {
    font-family: "Montserrat", Arial, sans-serif; font-weight: 500; color: var(--orange);
    font-size: 40px; line-height: 44px;
  }
  .brand__sub { display: block; font-size: 21px; line-height: 26px; padding-left: 6px; }

  .services {
    position: absolute; left: 30px; top: 147px; height: 375px;
    border-left: 5px solid var(--white);
    list-style: none; padding-left: 15px;
  }
  .services li {
    color: var(--white); font-size: 19px; font-weight: 400; line-height: 21px;
    text-transform: uppercase; margin-top: 19px;
  }
  .services li:first-child { margin-top: 6px; }

  .contact {
    position: absolute; left: 0; top: 565px; width: 988px; height: 74px;
    background: var(--orange-deep); color: var(--white);
  }
  .contact__item { position: absolute; display: flex; align-items: center; gap: 10px; top: 0; height: 74px; }
  .contact__address { left: 22px; font-size: 15px; line-height: 19px; }
  .contact__phone { left: 288px; font-size: 20px; }
  .contact__web { left: 478px; font-size: 16px; line-height: 19px; }
  .contact__url { font-weight: 700; font-size: 17px; }
  .contact__end { position: absolute; left: 0; top: 0; }
  .social { position: absolute; left: 795px; top: 12px; display: flex; gap: 9px; }
  .social span { width: 50px; height: 50px; border-radius: 50%; display: block; }
  .social .s1 { background: var(--social-a); }
  .social .s2 { background: var(--social-b); }
  .social .s3 { background: var(--social-c); }
</style>
</head>
<body>

<article class="ad ad--retail">
  <div class="promise">Your project should never sacrifice<br>time, quality, or price.<br><span class="promise__accent">That’s our promise.</span></div>
  <div class="headline">NEVER COMPROMISE</div>
  <div class="photo" role="img" aria-label="Aerial view of a completed retail center with white roofs and orange accent towers"></div>
  <div class="tagline">Your building. Your schedule. <span class="tagline__accent">Our skills.</span></div>
  <svg class="panel" viewBox="0 0 408 565" aria-hidden="true"><path d="M0 0 H370 A38 38 0 0 1 408 38 V395 A30 30 0 0 1 378 425 H358 A38 38 0 0 0 320 463 V565 H0 Z" fill="var(--navy)"/></svg>
  <div class="brand"><span class="brand__mark"></span><div class="brand__name">Marrowcrest<span class="brand__sub">Construction, Inc.</span></div></div>
  <ul class="services">
    <li>Construction + Planning</li><li>General Contracting</li><li>Tenant Improvements</li><li>Concrete Tilt Up</li><li>Single + Multi-Story</li><li>Wood Frame</li><li>Masonry</li><li>Steel + Curtain Wall</li><li>Maintenance Building +<br>Property</li>
  </ul>
  <footer class="contact">
    <svg class="contact__end" width="988" height="74" aria-hidden="true"><path d="M728 0 H988 V74 H790 C790 28 768 0 728 0 Z" fill="var(--navy)"/></svg>
    <div class="contact__item contact__address"><svg width="24" height="34" viewBox="0 0 24 34"><path d="M12 0 A12 12 0 0 1 24 12 C24 20 12 34 12 34 C12 34 0 20 0 12 A12 12 0 0 1 12 0 Z M12 7 A5 5 0 1 0 12.01 7 Z" fill="#fff" fill-rule="evenodd"/></svg><span>2870 Larkspur Ave., Suite 4<br>Riverton, CA 95610</span></div>
    <div class="contact__item contact__phone"><svg width="30" height="30" viewBox="0 0 24 24"><path d="M6.6 10.8a15 15 0 0 0 6.6 6.6l2.2-2.2a1 1 0 0 1 1-.25 11.4 11.4 0 0 0 3.6.57 1 1 0 0 1 1 1V20a1 1 0 0 1-1 1A17 17 0 0 1 3 4a1 1 0 0 1 1-1h3.5a1 1 0 0 1 1 1c0 1.25.2 2.45.57 3.57a1 1 0 0 1-.25 1z" fill="#fff"/></svg><span>555.210.4477</span></div>
    <div class="contact__item contact__web"><svg width="34" height="34" viewBox="0 0 34 34" fill="none" stroke="#fff" stroke-width="2"><circle cx="17" cy="17" r="15"/><ellipse cx="17" cy="17" rx="7" ry="15"/><path d="M2 17 H32 M5 9 H29 M5 25 H29"/></svg><span>View our projects:<br><span class="contact__url">marrowcrestbuilding.com</span></span></div>
    <div class="social"><span class="s1" role="img" aria-label="Social profile one"></span><span class="s2" role="img" aria-label="Social profile two"></span><span class="s3" role="img" aria-label="Social profile three"></span></div>
  </footer>
</article>

<article class="ad ad--tiltup">
  <div class="promise">Your project should never sacrifice<br>time, quality, or price.<br><span class="promise__accent">That’s our promise.</span></div>
  <div class="headline">NEVER COMPROMISE</div>
  <div class="photo" role="img" aria-label="Concrete tilt-up panels braced against a blue sky during construction"></div>
  <div class="tagline">Your building. Your schedule. <span class="tagline__accent">Our skills.</span></div>
  <svg class="panel" viewBox="0 0 408 565" aria-hidden="true"><path d="M0 0 H370 A38 38 0 0 1 408 38 V395 A30 30 0 0 1 378 425 H358 A38 38 0 0 0 320 463 V565 H0 Z" fill="var(--navy)"/></svg>
  <div class="brand"><span class="brand__mark"></span><div class="brand__name">Marrowcrest<span class="brand__sub">Construction, Inc.</span></div></div>
  <ul class="services">
    <li>Construction + Planning</li><li>General Contracting</li><li>Tenant Improvements</li><li>Concrete Tilt Up</li><li>Single + Multi-Story</li><li>Wood Frame</li><li>Masonry</li><li>Steel + Curtain Wall</li><li>Maintenance Building +<br>Property</li>
  </ul>
  <footer class="contact">
    <svg class="contact__end" width="988" height="74" aria-hidden="true"><path d="M728 0 H988 V74 H790 C790 28 768 0 728 0 Z" fill="var(--navy)"/></svg>
    <div class="contact__item contact__address"><svg width="24" height="34" viewBox="0 0 24 34"><path d="M12 0 A12 12 0 0 1 24 12 C24 20 12 34 12 34 C12 34 0 20 0 12 A12 12 0 0 1 12 0 Z M12 7 A5 5 0 1 0 12.01 7 Z" fill="#fff" fill-rule="evenodd"/></svg><span>2870 Larkspur Ave., Suite 4<br>Riverton, CA 95610</span></div>
    <div class="contact__item contact__phone"><svg width="30" height="30" viewBox="0 0 24 24"><path d="M6.6 10.8a15 15 0 0 0 6.6 6.6l2.2-2.2a1 1 0 0 1 1-.25 11.4 11.4 0 0 0 3.6.57 1 1 0 0 1 1 1V20a1 1 0 0 1-1 1A17 17 0 0 1 3 4a1 1 0 0 1 1-1h3.5a1 1 0 0 1 1 1c0 1.25.2 2.45.57 3.57a1 1 0 0 1-.25 1z" fill="#fff"/></svg><span>555.210.4477</span></div>
    <div class="contact__item contact__web"><svg width="34" height="34" viewBox="0 0 34 34" fill="none" stroke="#fff" stroke-width="2"><circle cx="17" cy="17" r="15"/><ellipse cx="17" cy="17" rx="7" ry="15"/><path d="M2 17 H32 M5 9 H29 M5 25 H29"/></svg><span>View our projects:<br><span class="contact__url">marrowcrestbuilding.com</span></span></div>
    <div class="social"><span class="s1" role="img" aria-label="Social profile one"></span><span class="s2" role="img" aria-label="Social profile two"></span><span class="s3" role="img" aria-label="Social profile three"></span></div>
  </footer>
</article>

</body>
</html>
```